Limousine Service Company Website

we need a website designed for a national limousine company with global capabilities (meaning they can service clients throughout the US and the world)

They service mostly corporate/business travelers, and groups and meetings, with a small portion of their business devoted to retail clients (special events and personal travel)

The overall look should be corporate, and we prefer a responsive design. We will need a home page, a fleet page (examples can be seen here: https://www.brqcarriage.com/fleet
http://www.pellowaychauffeurs.com/our-fleet) and one interior page

Copy will be lorem epsum for now

We have no logo yet but can put a placeholder logo

Industry/Entity Type

It Company

```html
<!DOCTYPE html>
<html lang="en">
<head>
<meta charset="utf-8">
<title>Silverline Limos</title>
<link href="https://fonts.googleapis.com/css2?family=Arimo:ital,wght@0,400;0,700;1,400&display=swap" rel="stylesheet">
<style>
:root{
  --gold:#c9a84c;
  --gold-light:#e6cf7e;
  --gold-dark:#b8933a;
  --ink:#222;
  --muted:#a9a9a9;
  --nav:#262626;
  --footer:#333;
  --line:#e4e4e4;
  --white:#fff;
}
*{box-sizing:border-box;margin:0;padding:0}
html,body{width:861px;height:1200px;overflow:hidden;background:var(--white)}
body{position:relative;font-family:"Arimo",Arial,sans-serif;color:var(--ink)}
.abs{position:absolute}
.nav{left:0;top:0;width:861px;height:33px;background:var(--nav);z-index:5}
.nav a{position:absolute;top:11px;font-size:10px;color:#eee;text-decoration:none;white-space:nowrap}
.nav .active{border-bottom:2px solid var(--gold);padding-bottom:10px}
.nav .call{left:698px}
.nav .call svg{vertical-align:-2px;margin-right:4px}
.hero{left:0;top:33px;width:861px;height:240px}
.car{left:381px;top:158px;width:301px;height:135px;border-radius:30px 50px 18px 18px;background:radial-gradient(ellipse at 50% 45%,#3a3a3a,#0d0d0d 75%);z-index:3}
.booking{left:70px;top:110px;width:240px;height:261px;border:3px solid var(--gold);background:var(--white);z-index:4}
.booking h2{height:34px;background:linear-gradient(#e1c26a,var(--gold));color:var(--white);font-size:14px;text-align:center;line-height:34px}
.booking label{position:absolute;left:9px;font-size:8px;font-weight:700}
.field{position:absolute;left:6px;width:222px;height:27px;border:1px solid #ccc;border-radius:3px;font-size:10px;color:#999;padding:7px 9px;white-space:nowrap}
.pick{position:absolute;top:160px;height:26px;border:1px solid #ccc;border-radius:3px;font-size:10px;padding:6px 7px;color:#222}
.pick i{position:absolute;right:0;top:0;width:22px;height:24px;background:var(--gold);border-radius:0 2px 2px 0}
.pick i::after{content:"";position:absolute;left:6px;top:7px;width:9px;height:9px;border:1px solid var(--white);border-radius:50%}
.btn{position:absolute;left:6px;top:199px;width:222px;height:26px;background:linear-gradient(#e0c36e,var(--gold-dark));border-radius:3px;color:var(--white);font-weight:700;font-size:14px;text-align:center;line-height:26px}
.help{position:absolute;left:0;top:237px;width:234px;text-align:center;font-size:8px;white-space:nowrap}
.h2{font-size:14px;color:var(--gold);font-weight:400;white-space:nowrap}
.copy{font-size:9.4px;line-height:12px;color:#222}
.benefits li{list-style:none;font-size:9.4px;height:20px;position:relative;padding-left:17px;white-space:nowrap}
.benefits li::before{content:"";position:absolute;left:0;top:1px;width:9px;height:9px;background:var(--gold);border-radius:50%}
.benefits li::after{content:"";position:absolute;left:3px;top:3px;width:2px;height:4px;border:solid var(--white);border-width:0 1.2px 1.2px 0;transform:rotate(45deg)}
.news-item{left:79px;width:222px;border-left:3px solid var(--gold);padding-left:11px;font-size:9px;line-height:11px}
.more{display:block;text-align:right;font-style:italic;color:var(--gold);margin-top:4px}
.rule{height:1px;background:var(--line)}
.quote .avatar{position:absolute;left:0;top:0;width:40px;height:40px;border-radius:50%;background:linear-gradient(#b9c4c2,#6f7d7b);box-shadow:0 0 0 3px #f0f0f0}
.quote p{position:absolute;left:52px;top:0;width:158px;font-size:9.2px;line-height:15.7px;color:var(--muted);text-align:justify;hyphens:auto;-webkit-hyphens:auto}
.quote b{position:absolute;left:52px;top:70px;font-size:9px;font-weight:400;color:#111;white-space:nowrap}
.pay{top:810px;font-size:22px;font-weight:700;color:#777;white-space:nowrap}
.footer{left:0;top:876px;width:861px;height:324px;background:var(--footer);border-top:3px solid var(--gold-light)}
.footer h3{font-size:11.5px;color:var(--gold);font-weight:400;margin-bottom:6px;white-space:nowrap}
.footer ul{list-style:none}
.footer li{font-size:9.6px;color:var(--white);height:18.4px;white-space:nowrap}
.info{right:97px;top:89px;text-align:right;font-size:9.6px;line-height:18.4px;color:var(--white);white-space:nowrap}
.social span{position:absolute;width:18px;height:18px;background:var(--gold);border-radius:2px}
.legal{left:68px;top:252px;width:470px;font-size:6.8px;line-height:12px;color:var(--white)}
</style>
</head>
<body>
<nav class="abs nav">
  <a style="left:356px" class="active">Home</a>
  <a style="left:409px">About Us</a>
  <a style="left:476px">Limos</a>
  <a style="left:529px">Our Services</a>
  <a style="left:611px">Contact Us</a>
  <a class="call"><svg width="9" height="9" viewBox="0 0 10 10"><circle cx="5" cy="5" r="4.3" fill="none" stroke="#c9a84c"/><path d="M3.3 2.8l1 .9-.5.8c.4.8.9 1.3 1.7 1.7l.8-.5.9 1-.7.8C4.8 7.3 2.9 5.4 2.6 3.6z" fill="#c9a84c"/></svg>Call Us: 01800. 442.907</a>
</nav>

<svg class="abs hero" viewBox="0 0 861 240" role="img" aria-label="Night city skyline behind the hero">
  <defs><linearGradient id="sky" x1="0" y1="0" x2="0" y2="1"><stop offset="0" stop-color="#4a4a4a"/><stop offset=".6" stop-color="#1f1f1f"/><stop offset="1" stop-color="#3a3a3a"/></linearGradient></defs>
  <rect width="861" height="240" fill="url(#sky)"/>
  <path d="M0 228 Q420 200 861 192 L861 240 L0 240Z" fill="#fff"/>
  <path d="M0 228 Q420 200 861 192" fill="none" stroke="#c9a84c" stroke-width="3"/>
</svg>
<div class="abs car" role="img" aria-label="Black luxury SUV"></div>

<section class="abs booking">
  <h2>Book Your Limosine</h2>
  <label style="top:50px">Pick-Up Location</label>
  <div class="field" style="top:63px">Enter Address or Airport Code</div>
  <label style="top:101px">Drop-Off Location</label>
  <div class="field" style="top:116px">Enter Address or Airport Code</div>
  <div class="pick" style="left:6px;width:97px">05/19/2014<i></i></div>
  <div class="pick" style="left:110px;width:65px">5pm<i></i></div>
  <div class="pick" style="left:182px;width:46px">00<i></i></div>
  <div class="btn">Calculate Prices</div>
  <p class="help">Having trouble? Call 1.800.552.319 for assistance.</p>
</section>

<h2 class="abs h2" style="left:357px;top:322px">Welcome to Silverline Limos</h2>
<div class="abs copy" style="left:357px;top:346px;width:356px">
  <p>Lorem ipsum dolor sit amet, consectetur adipisicing elit, sed do eiusmod tempor incididunt ut labore et dolore magna aliqua. Ut enim ad minim veniam, quis nostrud exercitation ullamco laboris nisi ut aliquip ex ea commodo consequat.</p>
  <p style="margin-top:4px">Duis aute irure dolor in reprehenderit in voluptate velit esse cillum dolore eu fugiat nulla pariatur. Excepteur sint occaecat cupidatat non proident, sunt in culpa qui officia deserunt mollit anim id est laborum.</p>
</div>

<h2 class="abs h2" style="left:357px;top:448px">Benefits</h2>
<ul class="abs benefits" style="left:357px;top:477px">
  <li>Lorem ipsum dolor sit amet, consectetur voluptate adipisicing elit.</li>
  <li>Duis aute irure dolor in reprehenderit in voluptate velit esse cillum dolore eu fugiat</li>
  <li>Lorem ipsum dolor sit amet, consectetur voluptate adipisicing elit.</li>
  <li>Duis aute irure dolor in reprehenderit in voluptate velit esse cillum dolore eu fugiat</li>
  <li>Lorem ipsum dolor sit amet, consectetur voluptate adipisicing elit.</li>
</ul>

<h2 class="abs h2" style="left:78px;top:395px">News and Updates</h2>
<div class="abs news-item" style="top:424px">Lorem ipsum dolor sit amet, consectetur adipisicing elit, sed do eiusmod tempor incididunt ut labore et dolore magna aliqua.<br>Ut enim ad minim veniam, quis nostrud exercitation<span class="more">read more</span></div>
<div class="abs rule" style="left:79px;top:494px;width:222px"></div>
<div class="abs news-item" style="top:505px">Lorem ipsum dolor sit amet, consectetur adipisicing elit, sed do eiusmod tempor incididunt ut labore et dolore magna aliqua.<br>Ut enim ad minim veniam, quis nostrud exercitation<span class="more">read more</span></div>
<div class="abs rule" style="left:79px;top:577px;width:222px"></div>
<p class="abs" style="left:89px;top:584px;font-size:9px;font-style:italic;color:var(--gold);white-space:nowrap">Read all The News and Update</p>

<h2 class="abs h2" style="left:77px;top:627px">Testimonials</h2>
<div class="abs rule" style="left:77px;top:650px;width:682px"></div>
<div class="abs quote" style="left:79px;top:668px"><div class="avatar" role="img" aria-label="Client portrait"></div><p>“Lorem ipsum dolor sit amet, consectetur adipisicing elit, sed do eiusmod tempor incididunt ut labore et dolore magna aliqua. Ut enim ad mini”</p><b>By Marcus Dell</b></div>
<div class="abs quote" style="left:315px;top:668px"><div class="avatar" role="img" aria-label="Client portrait"></div><p>“Lorem ipsum dolor sit amet, consectetur adipisicing elit, sed do eiusmod tempor incididunt ut labore et dolore magna aliqua. Ut enim ad mini”</p><b>By Marcus Dell</b></div>
<div class="abs quote" style="left:558px;top:668px"><div class="avatar" role="img" aria-label="Client portrait"></div><p>“Lorem ipsum dolor sit amet, consectetur adipisicing elit, sed do eiusmod tempor incididunt ut labore et dolore magna aliqua. Ut enim ad mini”</p><b>By Marcus Dell</b></div>
<div class="abs rule" style="left:120px;top:771px;width:630px"></div>

<span class="abs pay" style="left:284px">Paywell</span>
<span class="abs pay" style="left:394px">Cardia</span>
<span class="abs pay" style="left:476px">Meridian</span>
<span class="abs pay" style="left:580px">Kinto</span>

<footer class="abs footer">
  <div class="abs" style="left:71px;top:29px"><h3>Get to Know Us</h3><ul><li>Lorem ipsum dolor</li><li>The Limo Difference</li><li>Car Service Fleet</li><li>Our Limo Service Rates</li><li>Our Car Service App</li><li>Management Team</li><li>Press</li><li>Blog</li></ul></div>
  <div class="abs" style="left:212px;top:29px"><h3>Products and Services</h3><ul><li>Lorem ipsum dolor</li><li>The Limo Difference</li><li>Car Service Fleet</li><li>Our Limo Service Rates</li><li>Our Car Service App</li><li>Management Team</li><li>Press</li><li>Blog</li></ul></div>
  <div class="abs" style="left:376px;top:29px"><h3>Get to Know Us</h3><ul><li>Lorem ipsum dolor</li><li>The Limo Difference</li><li>Car Service Fleet</li></ul><h3 style="margin-top:3px">Get to Know Us</h3><ul><li>Lorem ipsum dolor</li><li>The Limo Difference</li><li>Car Service Fleet</li></ul></div>
  <p class="abs" style="left:667px;top:51px;font-size:10px;color:var(--white)">YOUR LOGO</p>
  <div class="abs info">Corporate Headquarters: 1-800-418-2270<br>Customer Service: 1-800-935-4108<br>Carrow Fleet Group LLC<br>58 Harlow Avenue<br>Fairmont, ST 20417</div>
  <div class="abs social" style="left:0;top:0"><span style="left:692px;top:192px"></span><span style="left:719px;top:192px"></span><span style="left:746px;top:192px"></span></div>
  <div class="abs" style="left:68px;top:201px;width:65px;height:26px;background:#1d4f7c;border-radius:3px"></div>
  <p class="abs legal">Lorem ipsum dolor sit amet, consectetur adipisicing elit, sed do eiusmod tempor incididunt ut labore et dolore magna aliqua. Ut enim ad minim veniam, quis nostrud exercitation ullamco laboris nisi ut aliquip ex ea commodo consequat. Duis aute irure dolor in reprehenderit in voluptate velit esse cillum dolore eu fugiat nulla pariatur. Excepteur sint occaecat cupidatat non proident, sunt in culpa qui officia deserunt mollit anim id est<br>© Copyright 2014 Carrow Fleet Group LLC</p>
</footer>
</body>
</html>
```